Need Edgy Web Design Home Page for Entertainment Agency

We need a web design splash page for our entertainment company, Velvet Crown Agency based (Los Angeles and New York).
Velvet Crown is a full service PR, marketing and special events agency based in Los Angeles and New York. We aim to serve the most elite in entertainment, media and sports.

With a combined experience of over 30 years in the entertainment industry, our team is committed to deliver each client with the upmost service and contemporary strategies to increase your business objective.

CREATIVE, EDGY & TRENDSETTING

SERVICES

PR Campaigns

Media Relations

Talent Representation

Brand Marketing & Activations

Special Events: Publicity & Consulting

EXPERTISE

Television

Film

Talent

Music

Marketing & Promotions

Industry Events

Digital & Social Media

Looking for a home page that is flashy, edgy and creative. I've provided our logos and contact details:

Delia Varga
dvarga@velcrowmla.com

Jonah Pryce
jpryce@velcrowmny.com

Renata Olmos
rolmos@velcrowmla.com

Target Market(s)

Los Angeles and New York

Industry/Entity Type

Entertainment

Number of Pages Required

1 page

Font styles to use
Serif
Decorative

Requirements
Must have
• 1. Logo
• 2. Description of services but done creatively
• 4. Visuals (Stock images: cool edgy millennials & graphics images that make sense for our agency)
• 5. Contact Details
• Reference: https://www.tunelatchery.net & http://www.thekestrelworks.com
Nice to have
• If possible would love to have stock cartoon images included as images of Delia and I. Reference image (http://www.pixmarrowfield.com/pic-507314862/stock-vector-cute-cartoon-characters-young-boy-and-girl-in-cool-casual-outfits.html)
Should not have
• Should not look boring!

```html
<!DOCTYPE html>
<html lang="en">
<head>
<meta charset="utf-8">
<title>Velvet Crown Agency</title>
<link href="https://fonts.googleapis.com/css2?family=Lato:wght@300;400;700&family=Playfair+Display:wght@700&display=swap" rel="stylesheet">
<style>
:root{
  --dark:#2a2824;
  --dark-2:#35322c;
  --gold:#c9a24a;
  --gold-light:#e2c577;
  --tan:#dccfa6;
  --tan-2:#e8ddbb;
  --paper:#f4f3f1;
  --ink:#3a3833;
  --muted:#6d6a63;
  --white:#ffffff;
}
*{margin:0;padding:0;box-sizing:border-box}
html,body{width:1200px;height:3084px;overflow:hidden}
body{font-family:"Lato",Arial,sans-serif;color:var(--ink);background:var(--paper);position:relative}
.abs{position:absolute}
.section-title{position:absolute;left:0;width:1200px;text-align:center;font-weight:300;font-size:34px;letter-spacing:1px;text-transform:uppercase}
.section-title::after{content:"";display:block;width:90px;height:2px;background:var(--gold);margin:10px auto 0}

/* hero */
.hero{left:0;top:0;width:1200px;height:820px;background:linear-gradient(180deg,#8d9390 0%,#a9aca6 40%,#7e8c6a 75%,#6b7a56 100%)}
.nav{left:0;top:0;width:1200px;height:110px;background:linear-gradient(180deg,rgba(0,0,0,.45),rgba(0,0,0,0))}
.brand{left:120px;top:30px;display:flex;align-items:center;gap:12px;font-family:"Playfair Display",Georgia,serif;font-size:34px;color:var(--white)}
.brand-dot{width:34px;height:34px;border-radius:50%;background:var(--gold)}
.menu{right:120px;top:38px;display:flex;gap:8px}
.menu a{color:var(--white);text-decoration:none;font-size:14px;padding:8px 16px}
.menu a.active{background:var(--gold);color:var(--dark)}

/* about */
.about{left:0;top:820px;width:1200px;height:308px;background:linear-gradient(135deg,#fbfbfa,#ececea)}
.about .section-title{top:60px;color:#2f2d29}
.about p{position:absolute;left:230px;width:740px;text-align:center;font-size:14px;line-height:22px;color:var(--muted)}

/* services */
.services{left:0;top:1128px;width:1200px;height:452px;background:var(--dark)}
.services .section-title{top:40px;color:var(--white)}
.service{position:absolute;left:600px;width:400px;padding-left:62px}
.service .icon{position:absolute;left:0;top:2px;width:46px;height:46px;border-radius:50%;background:var(--gold);border:3px solid #e7d39a}
.service h3{font-size:16px;font-weight:400;color:var(--gold-light);margin-bottom:5px}
.service p{font-size:11px;line-height:15px;color:#d6d2c8}

/* expertise */
.expertise{left:0;top:1580px;width:1200px;height:820px;background:linear-gradient(180deg,var(--tan-2),var(--tan))}
.expertise .section-title{top:60px;color:#2f2d29}
.expertise .sub{position:absolute;top:126px;left:0;width:1200px;text-align:center;font-size:13px;color:var(--ink)}
.spine{left:599px;top:1740px;width:2px;height:600px;background:#8a7a52}
.exp{position:absolute;width:320px;font-size:12px;line-height:17px;color:var(--ink)}
.exp h3{font-size:15px;font-weight:400;text-transform:uppercase;margin-bottom:4px}
.exp b{font-weight:700}
.exp.left{left:115px;text-align:right}
.exp.right{left:765px}
.exp-icon{position:absolute;width:60px;height:60px;border-radius:50%;background:var(--dark);border:3px solid var(--gold)}
.exp-icon svg{position:absolute;left:15px;top:15px}

/* social */
.social{left:0;top:2400px;width:1200px;height:140px;background:linear-gradient(180deg,#3a3732,#2a2824)}
.follow{position:absolute;top:2436px;width:288px;height:68px;background:#1f1d1a;border:1px solid #5a554b;display:flex;align-items:center;gap:14px;padding-left:18px;color:var(--white)}
.follow .sq{width:36px;height:36px;background:#5a554b}
.follow strong{display:block;font-size:15px;font-weight:400}
.follow span{font-size:11px;letter-spacing:1px;color:#c9c3b5}

/* team */
.team{left:0;top:2540px;width:1200px;height:360px;background:linear-gradient(135deg,#fafaf9,#ebebe9)}
.team .section-title{top:40px;color:#2f2d29}
.team .sub{position:absolute;top:104px;left:0;width:1200px;text-align:center;font-size:13px;color:var(--muted)}
.member{position:absolute;top:2680px;width:300px;height:180px}
.avatar{position:absolute;left:0;top:0;width:86px;height:86px;border-radius:50%;background:linear-gradient(135deg,#c8a57e,#6d5a48)}
.member .info{position:absolute;left:104px;top:6px;font-size:11px;line-height:16px;color:var(--muted)}
.member h4{font-size:15px;font-weight:700;color:var(--ink)}
.member .role{font-size:12px;color:var(--ink);margin-bottom:3px}
.member .more{position:absolute;left:104px;top:118px;width:108px;height:26px;background:var(--gold);color:var(--white);font-size:11px;line-height:26px;text-align:center}

/* footer */
.footer{left:0;top:2900px;width:1200px;height:184px;background:linear-gradient(180deg,#d8b865,#b8913d)}
.foot-menu{left:130px;top:50px;display:flex;gap:42px;font-size:14px;color:var(--dark)}
.foot-contact{left:700px;top:32px;font-size:14px;line-height:34px;color:var(--dark)}
.foot-contact div{display:flex;align-items:center;gap:12px}
.foot-rule{left:130px;top:118px;width:940px;height:1px;background:rgba(42,40,36,.35)}
.copy{left:0;top:140px;width:1200px;text-align:center;font-size:12px;color:var(--dark)}
</style>
</head>
<body>

<div class="abs hero" role="img" aria-label="Photo of a young man in a suit riding a bicycle past a glass office building"></div>
<header class="abs nav"></header>
<div class="abs brand"><span class="brand-dot"></span>Velvet Crown</div>
<nav class="abs menu">
  <a class="active">Home</a><a>About Us</a><a>Services</a><a>Expertise</a><a>Contact Us</a>
</nav>

<section class="abs about">
  <h2 class="section-title">About Velvet Crown</h2>
  <p style="top:150px">Velvet Crown is a full service PR, marketing and special events agency based in Los Angeles and New York. We aim to serve the most elite in entertainment, media and sports.</p>
  <p style="top:204px">With a combined experience of over 30 years in the entertainment industry, our team is committed to deliver each client with the upmost service and contemporary strategies to increase your business objective.</p>
</section>

<section class="abs services">
  <h2 class="section-title">Our Services</h2>
</section>
<svg class="abs" style="left:130px;top:1230px" width="440" height="330" viewBox="0 0 440 330">
  <g fill="none" stroke="#c9a24a" stroke-width="2">
    <line x1="370" y1="30" x2="470" y2="30"/>
    <line x1="385" y1="100" x2="470" y2="100"/>
    <line x1="390" y1="165" x2="470" y2="165"/>
    <line x1="385" y1="230" x2="470" y2="230"/>
    <line x1="370" y1="300" x2="470" y2="300"/>
  </g>
  <circle cx="210" cy="165" r="172" fill="none" stroke="#c9a24a" stroke-width="8" stroke-dasharray="420 700" transform="rotate(-70 210 165)"/>
  <circle cx="210" cy="165" r="160" fill="#e9e7e2"/>
  <g stroke="#2a2824" stroke-width="3">
    <line x1="210" y1="165" x2="210" y2="5"/>
    <line x1="210" y1="165" x2="362" y2="116"/>
    <line x1="210" y1="165" x2="304" y2="294"/>
    <line x1="210" y1="165" x2="116" y2="294"/>
    <line x1="210" y1="165" x2="58" y2="116"/>
  </g>
  <circle cx="210" cy="165" r="72" fill="#2a2824"/>
  <circle cx="210" cy="165" r="58" fill="#c9a24a"/>
  <text x="210" y="170" text-anchor="middle" font-family="Lato, sans-serif" font-size="13" fill="#2a2824">Velvet Crown</text>
  <g font-family="Lato, sans-serif" font-size="12" fill="#3a3833" text-anchor="middle">
    <text x="258" y="62" transform="rotate(18 258 62)">Media Relations</text>
    <text x="310" y="185" transform="rotate(80 310 185)">Talent Rep.</text>
    <text x="210" y="292">Brand Marketing</text>
    <text x="110" y="185" transform="rotate(-62 110 185)">Special Events</text>
    <text x="150" y="70" transform="rotate(-30 150 70)">PR Campaigns</text>
  </g>
</svg>
<div class="service" style="top:1238px"><span class="icon"></span><h3>PR Campaigns</h3><p>Lorem ipsum dolor sit amet, consectetuer adipiscing elit, sed diam nonummy nibh euismod tincidunt ut laoreet dolore.</p></div>
<div class="service" style="top:1308px"><span class="icon"></span><h3>Media Relations</h3><p>Lorem ipsum dolor sit amet, consectetuer adipiscing elit, sed diam nonummy nibh euismod tincidunt ut laoreet dolore.</p></div>
<div class="service" style="top:1373px"><span class="icon"></span><h3>Talent Representation</h3><p>Lorem ipsum dolor sit amet, consectetuer adipiscing elit, sed diam nonummy nibh euismod tincidunt ut laoreet dolore.</p></div>
<div class="service" style="top:1438px"><span class="icon"></span><h3>Brand Marketing &amp; Activations</h3><p>Lorem ipsum dolor sit amet, consectetuer adipiscing elit, sed diam nonummy nibh euismod tincidunt ut laoreet dolore.</p></div>
<div class="service" style="top:1508px"><span class="icon"></span><h3>Special Events - Publicity &amp; Consulting</h3><p>Lorem ipsum dolor sit amet, consectetuer adipiscing elit, sed diam nonummy nibh euismod tincidunt ut laoreet dolore.</p></div>

<section class="abs expertise">
  <h2 class="section-title">Our Expertise</h2>
  <p class="sub">Lorem ipsum dolor sit amet consectetuer adipiscing</p>
</section>
<div class="abs spine"></div>

<div class="exp left" style="top:1772px"><h3>Television</h3>Lorem ipsum dolor sit amet, consectetuer adipiscing elit, sed diam nonummy nibh euismod tincidunt.<br><b>Lorem ipsum dolor sit amet</b></div>
<div class="exp-icon" style="left:460px;top:1780px"><svg width="30" height="30" viewBox="0 0 30 30"><rect x="3" y="6" width="24" height="16" fill="none" stroke="#c9a24a" stroke-width="2"/><line x1="10" y1="26" x2="20" y2="26" stroke="#c9a24a" stroke-width="2"/></svg></div>

<div class="exp right" style="top:1856px"><h3>Music</h3>Lorem ipsum dolor sit amet, consectetuer adipiscing elit, sed diam nonummy nibh euismod tincidunt.<br><b>Lorem ipsum dolor sit amet</b></div>
<div class="exp-icon" style="left:680px;top:1862px"><svg width="30" height="30" viewBox="0 0 30 30"><circle cx="10" cy="22" r="4" fill="#c9a24a"/><line x1="14" y1="22" x2="14" y2="5" stroke="#c9a24a" stroke-width="2"/><line x1="14" y1="5" x2="23" y2="9" stroke="#c9a24a" stroke-width="2"/></svg></div>

<div class="exp left" style="top:1994px"><h3>Film</h3>Lorem ipsum dolor sit amet, consectetuer adipiscing elit, sed diam nonummy nibh euismod tincidunt.<br><b>Lorem ipsum dolor sit amet</b></div>
<div class="exp-icon" style="left:460px;top:2000px"><svg width="30" height="30" viewBox="0 0 30 30"><rect x="3" y="7" width="24" height="16" fill="none" stroke="#c9a24a" stroke-width="2"/><polygon points="12,11 20,15 12,19" fill="#c9a24a"/></svg></div>

<div class="exp right" style="top:2024px"><h3>Marketing &amp; Promotions</h3>Lorem ipsum dolor sit amet, consectetuer adipiscing elit, sed diam nonummy nibh euismod tincidunt.<br><b>Lorem ipsum dolor sit amet</b></div>
<div class="exp-icon" style="left:680px;top:2030px"><svg width="30" height="30" viewBox="0 0 30 30"><circle cx="15" cy="15" r="5" fill="#c9a24a"/><circle cx="5" cy="8" r="3" fill="#c9a24a"/><circle cx="25" cy="8" r="3" fill="#c9a24a"/><circle cx="15" cy="27" r="3" fill="#c9a24a"/></svg></div>

<div class="exp left" style="top:2150px"><h3>Talent</h3>Lorem ipsum dolor sit amet, consectetuer adipiscing elit, sed diam nonummy nibh euismod tincidunt.<br><b>Lorem ipsum dolor sit amet</b></div>
<div class="exp-icon" style="left:460px;top:2156px"><svg width="30" height="30" viewBox="0 0 30 30"><polygon points="15,3 18,12 27,12 20,18 23,27 15,21 7,27 10,18 3,12 12,12" fill="#c9a24a"/></svg></div>

<div class="exp right" style="top:2200px"><h3>Industry Events</h3>Lorem ipsum dolor sit amet, consectetuer adipiscing elit, sed diam nonummy nibh euismod tincidunt.<br><b>Lorem ipsum dolor sit amet</b></div>
<div class="exp-icon" style="left:680px;top:2206px"><svg width="30" height="30" viewBox="0 0 30 30"><rect x="4" y="7" width="22" height="19" fill="none" stroke="#c9a24a" stroke-width="2"/><line x1="4" y1="12" x2="26" y2="12" stroke="#c9a24a" stroke-width="2"/></svg></div>

<section class="abs social"></section>
<div class="follow" style="left:132px"><span class="sq"></span><div><strong>Follow Us</strong><span>@VELVETCROWN</span></div></div>
<div class="follow" style="left:456px"><span class="sq"></span><div><strong>Follow Us</strong><span>@VELVETCROWN</span></div></div>
<div class="follow" style="left:780px"><span class="sq"></span><div><strong>Connect Us</strong><span>VELVET CROWN</span></div></div>

<section class="abs team">
  <h2 class="section-title">Our Team</h2>
  <p class="sub">Lorem ipsum dolor sit amet consectetuer adipiscing</p>
</section>
<div class="member" style="left:140px">
  <div class="avatar" role="img" aria-label="Portrait of Jonah Pryce"></div>
  <div class="info"><h4>Jonah Pryce</h4><div class="role">President</div>Ph: 310 555 0192<br>jpryce@velcrowmny.com</div>
  <div class="more">Learn more</div>
</div>
<div class="member" style="left:460px">
  <div class="avatar" role="img" aria-label="Portrait of Delia Varga"></div>
  <div class="info"><h4>Delia Varga</h4><div class="role">President</div>Ph: 310 555 0192<br>dvarga@velcrowmla.com</div>
  <div class="more">Learn more</div>
</div>
<div class="member" style="left:780px">
  <div class="avatar" role="img" aria-label="Portrait of Renata Olmos"></div>
  <div class="info"><h4>Renata Olmos</h4><div class="role">Partner &amp; Legal Counsel</div>Ph: 310 555 0192<br>rolmos@velcrowmla.com</div>
  <div class="more">Learn more</div>
</div>

<footer class="abs footer">
  <nav class="abs foot-menu"><span>Home</span><span>About Us</span><span>Services</span><span>Expertise</span><span>Contact Us</span></nav>
  <div class="abs foot-contact">
    <div><svg width="18" height="18" viewBox="0 0 18 18"><path d="M4 2 L7 2 L8 6 L6 7.5 Q8 11 10.5 12 L12 10 L16 11 L16 14 Q15 16 12 16 Q3 14 2 5 Q2 2 4 2Z" fill="#2a2824"/></svg>+1 310 555 0148</div>
    <div><svg width="18" height="18" viewBox="0 0 18 18"><rect x="1" y="4" width="16" height="11" fill="none" stroke="#2a2824" stroke-width="1.6"/><polyline points="1,4 9,10 17,4" fill="none" stroke="#2a2824" stroke-width="1.6"/></svg>info@velvetcrown.com</div>
  </div>
  <div class="abs foot-rule"></div>
  <div class="abs copy">Copyright © 2015 Velvet Crown | All Rights Reserved.</div>
</footer>

</body>
</html>
```